Your complete Gardening and lawn maintenance, Horticultural care. (to be on card)
We are looking at using a logo of a tree, with a recycling emblem circling the tree. The colors of choice, are burnt oranges and olive greens. Presented; simple to the eye, yet catchy to the clients in a eco-friendly way. We have uploaded a design for you to look at just to give a rough idea, you can use that or create your own ideas or play around with a mixture.

Target Market(s)

Home owners, businesses, real estates.

Industry/Entity Type

Recycling

Contact Information for Business Card

Name: Derek Ostrowe
Phone: 0421583906
Email: bramblewoodyards@mailnest.net

Logo Text

Bramble-Wood Yards

Logo styles of interest
Emblem Logo
Pictorial/Combination Logo
Abstract Logo
Requirements
Must have
• Business name: Bramble-Wood Yards
and slogan : Your complete Gardening and lawn maintenance, Horticultural care

```html
<!DOCTYPE html>
<html lang="en">
<head>
<meta charset="utf-8">
<title>Bramble-Wood Yards – Business Card</title>
<link rel="stylesheet" href="https://fonts.googleapis.com/css2?family=Marcellus&family=Alegreya:wght@400&family=Source+Sans+3:wght@400;600&display=swap">
<style>
  :root {
    --paper: #ffffff;
    --frame: #3a3a3a;
    --olive: #5f7a22;
    --olive-light: #9fb13c;
    --rule: #b5c335;
    --maroon: #4a1019;
  }
  html, body {
    margin: 0;
    padding: 0;
    width: 1200px;
    height: 703px;
    overflow: hidden;
    background: var(--paper);
  }
  .card {
    position: relative;
    width: 1200px;
    height: 703px;
    background: var(--paper);
  }
  .card__frame {
    position: absolute;
    left: 33px;
    top: 33px;
    width: 1134px;
    height: 637px;
    border: 1.5px solid var(--frame);
    box-sizing: border-box;
  }
  .brand-mark {
    position: absolute;
    left: 85px;
    top: 81px;
    width: 364px;
    height: 364px;
  }
  .brand-name {
    position: absolute;
    left: 488px;
    top: 118px;
    margin: 0;
    font-family: "Marcellus", serif;
    font-weight: 400;
    font-size: 74px;
    line-height: 86px;
    letter-spacing: 1px;
    color: var(--maroon);
    text-transform: uppercase;
  }
  .brand-name span { display: block; }
  .divider {
    position: absolute;
    left: 500px;
    top: 324px;
    width: 528px;
    height: 3px;
    background: var(--rule);
  }
  .tagline {
    position: absolute;
    left: 500px;
    top: 338px;
    margin: 0;
    font-family: "Alegreya", serif;
    font-size: 29px;
    line-height: 36px;
    color: var(--maroon);
  }
  .contact-name {
    position: absolute;
    left: 500px;
    top: 468px;
    margin: 0;
    font-family: "Source Sans 3", sans-serif;
    font-size: 28px;
    letter-spacing: 1.5px;
    color: var(--olive);
    text-transform: uppercase;
  }
  .contact-name .first { font-weight: 600; }
  .contact-name .last { font-weight: 400; }
  .contact-list {
    position: absolute;
    left: 500px;
    top: 540px;
    margin: 0;
    padding: 0;
    list-style: none;
    font-family: "Source Sans 3", sans-serif;
    font-size: 30px;
    line-height: 42px;
    color: var(--maroon);
  }
  .contact-list .label { font-weight: 600; }
</style>
</head>
<body>
<main class="card">
  <div class="card__frame"></div>

  <svg class="brand-mark" viewBox="0 0 364 364" aria-hidden="true">
    <circle cx="182" cy="182" r="170" fill="var(--olive-light)"/>
  </svg>

  <h1 class="brand-name"><span>Bramble-Wood</span><span>Yards</span></h1>

  <div class="divider"></div>

  <p class="tagline">Your complete Gardening and<br>Lawn Maintenance, Horticulture Care</p>

  <p class="contact-name"><span class="first">Derek</span> <span class="last">Ostrowe</span></p>

  <ul class="contact-list">
    <li><span class="label">TEL:</span> 042 158 3906</li>
    <li><span class="label">EMAIL:</span> bramblewoodyards@mailnest.net</li>
  </ul>
</main>
</body>
</html>
```